Lumo Pharma Chinese Traditional Medicine Web Design

We need a web design for a new company based in Shanghai China called 'Lumo Pharma'. We develop Chinese traditional herbal medicine, including research and development, technical support service, manufacturing, . Also, there’s a small ratio of western medicine. Our goal is to contributing to a healthier future.

Target Market(s)

global,but mainly China

Industry/Entity Type

Pharmaceutical

Number of Pages Required

1 page

Font styles to use
Serif

Colors
e4daeb
cedeed
cadf82
eaf2ce
fbd4d5
fee3d4
fabb94
fee18a
b8a6cd

Requirements
Must have
• triditional Chinese elements, concept of herbal, health, value, better life for people..could be colourful but not more than 3 different colour..
Nice to have
• Style: simple, communicate traditional Chinese herbal medicine element, as well as modern technique..same as LOGO style..
Should not have
• please dont show more IT elements...

```html
<!DOCTYPE html>
<html lang="en">
<head>
<meta charset="utf-8">
<title>Lumo Pharma — Chinese Traditional Medicine</title>
<link href="https://fonts.googleapis.com/css2?family=Libre+Baskerville&family=Noto+Serif+SC:wght@400&family=Poppins:wght@300;400;600&display=swap" rel="stylesheet">
<style>
:root{
  --brown:#7a4429;
  --brown-dark:#6e3e26;
  --bg:#f2f2f6;
  --bg-news:#f7f7fa;
  --text:#5b5553;
  --white:#ffffff;
}
*{margin:0;padding:0;box-sizing:border-box}
html,body{width:1200px;height:3372px;overflow:hidden}
body{position:relative;background:linear-gradient(#efeff5 0,#f4f4f8 1000px,#fafafc 1800px);font-family:"Poppins",sans-serif;color:var(--text)}
.abs{position:absolute}
.serif{font-family:"Libre Baskerville","Noto Serif SC",serif}
.zh{font-family:"Noto Serif SC",serif}
p{font-size:12.5px;line-height:21px;font-weight:300}
.btn{position:absolute;display:flex;align-items:center;justify-content:center;background:var(--brown);color:var(--white);border-radius:24px;font-size:11.5px;font-weight:600;letter-spacing:.2px;box-shadow:0 8px 16px rgba(122,68,41,.25)}
.section-title{color:var(--brown);font-size:25px;letter-spacing:.5px}
.section-title .zh{color:#6b6360;margin-left:14px;font-size:25px}

/* header */
.brand{left:114px;top:78px;display:flex;align-items:center;gap:10px;color:var(--brown);font-size:20px}
.brand-dot{width:14px;height:14px;border-radius:50%;background:var(--brown)}
.contact-line{top:56px;font-size:13px;display:flex;align-items:center;gap:8px}
.nav{top:92px;left:559px;display:flex;gap:29px;font-size:12.5px;color:#6b6360}
.nav .active{color:var(--brown)}

/* hero */
.hero-title{left:113px;top:352px;font-size:66px;color:var(--brown);letter-spacing:1px}
.hero-sub{left:113px;top:425px;font-size:24px;color:var(--brown)}
.hero-img{left:520px;top:170px;width:570px;height:590px;border-radius:40% 40% 45% 45%;background:radial-gradient(circle at 40% 55%,#b7772f 0,#8e5a2c 30%,#d9c79a 55%,rgba(242,242,246,0) 72%)}

/* overview */
.overview-img{left:65px;top:910px;width:445px;height:353px;border-radius:45%;background:radial-gradient(circle at 45% 55%,#7d3b22 0,#3a2a22 35%,#c9a66b 60%,rgba(242,242,246,0) 72%)}

/* products */
.card{position:absolute;width:232px;border-radius:8px;padding:26px 28px}
.card h3{font-family:"Poppins",sans-serif;font-weight:400;font-size:16px;line-height:21px}
.card .zh{font-size:17px;margin:4px 0 18px;display:block}
.card p{font-size:12px;line-height:20.5px}
.card-fill{left:545px;top:1352px;height:317px;background:var(--brown);color:var(--white)}
.card-line{left:823px;top:1398px;height:310px;border:2px solid var(--brown);background:var(--white);color:var(--brown)}
.card-line p{color:var(--text)}

/* news */
.news-band{left:0;top:1806px;width:1200px;height:655px;background:var(--bg-news)}
.news-img{width:229px;height:229px;border-radius:8px}
.news-text{width:160px}
.news-date{font-size:9.5px;color:var(--brown)}
.news-title{font-size:16px;color:var(--brown);margin-top:12px}
.news-zh{font-size:17px;color:#6b6360;margin:2px 0 20px}

/* contact */
.contact{left:0;top:2461px;width:1200px;height:556px;background:#f1ece6}
.contact-left{left:0;top:2461px;width:340px;height:556px;background:linear-gradient(100deg,#c78a3f 0,#d9a55a 50%,rgba(241,236,230,0) 100%)}
.contact-right{left:880px;top:2461px;width:320px;height:556px;background:linear-gradient(260deg,#7d3a20 0,#a9663a 45%,rgba(241,236,230,0) 100%)}
.field{position:absolute;background:var(--white);border-radius:22px;font-size:12px;padding:14px 24px;color:#6b6360;box-shadow:0 2px 8px rgba(0,0,0,.04)}

/* footer */
.footer{left:0;top:3017px;width:1200px;height:355px;background:var(--brown-dark);color:var(--white)}
.f-brand{left:114px;top:3130px;display:flex;align-items:center;gap:10px;font-size:20px;color:var(--white)}
.f-dot{width:14px;height:14px;border-radius:50%;background:var(--white)}
.f-h{font-size:15px;font-weight:400}
.f-zh{font-size:17px}
.f-small{font-size:11px;line-height:20.5px}
</style>
</head>
<body>

<!-- header -->
<div class="abs brand serif"><span class="brand-dot"></span>Lumo Pharma</div>
<div class="abs contact-line" style="left:789px;color:var(--brown)">
  <svg width="14" height="14" viewBox="0 0 24 24"><path fill="#7a4429" d="M6.6 10.8a15 15 0 006.6 6.6l2.2-2.2c.3-.3.7-.4 1-.2 1.1.4 2.3.6 3.6.6.6 0 1 .4 1 1V20c0 .6-.4 1-1 1A17 17 0 013 4c0-.6.4-1 1-1h3.5c.6 0 1 .4 1 1 0 1.3.2 2.5.6 3.6.1.3 0 .7-.2 1z"/></svg>
  +12 (555) 01-23-456
</div>
<div class="abs contact-line" style="left:982px;color:#6b6360">
  <svg width="14" height="11" viewBox="0 0 24 18"><rect width="24" height="18" rx="2" fill="#7a4429"/><path d="M2 3l10 7 10-7" stroke="#fff" stroke-width="2" fill="none"/></svg>
  hello@lumo.example
</div>
<nav class="abs nav">
  <span class="active">Home</span><span>Company overall</span><span>News</span><span>Products &amp; Services</span><span>Career</span><span>Contact us</span>
</nav>

<!-- hero -->
<h1 class="abs hero-title serif" style="font-weight:400">CHINESE</h1>
<div class="abs hero-sub serif">TRADITIONAL MEDICINE</div>
<p class="abs" style="left:113px;top:472px;width:345px">We develop Chinese traditional herbal medicine, including research and development, technical support service, manufacturing.</p>
<p class="abs" style="left:113px;top:555px;width:345px">. Also, there’s a small ratio of western medicine. Our goal is to contributing to a healthier future.</p>
<div class="btn" style="left:111px;top:623px;width:186px;height:46px">GET STARTED</div>
<div class="abs hero-img" role="img" aria-label="Bowl of dried Chinese herbs beside an acupuncture model figure"></div>

<!-- overview -->
<div class="abs overview-img" role="img" aria-label="Clay herbal pot with a bamboo tray of dried mushrooms, dates and roots"></div>
<div class="abs section-title serif" style="left:545px;top:1000px">OVERVIEW<span class="zh">總覽</span></div>
<p class="abs" style="left:545px;top:1052px;width:548px">Lumo Pharma is a pharmaceutical company registered in Shanghai China, 2019, committed to Chinese traditional herbal medicine, including research and development, technical support service, manufacturing, with top expert team. Also, there’s a small ratio of western medicine.</p>
<p class="abs" style="left:545px;top:1155px;width:548px">The special feature of Chinese traditional medicine is that, it would not only cure diseases, but also keep people away from diseases, with thousands of year practical experience. Our goal is to contributing to a healthier future.</p>

<!-- products -->
<div class="abs section-title serif" style="right:718px;top:1393px;text-align:right">PRODUCTS &amp; SERVICES</div>
<div class="abs zh" style="right:718px;top:1423px;font-size:25px;color:var(--brown)">產品和服務</div>
<p class="abs" style="right:720px;top:1482px;width:300px;text-align:right">Lumo Pharma is a pharmaceutical company registered in Shanghai China, 2019,</p>

<div class="card card-fill">
  <svg width="76" height="76" viewBox="0 0 76 76" fill="none" stroke="#fff" stroke-width="2">
    <circle cx="32" cy="40" r="14"/><circle cx="32" cy="40" r="8"/><path d="M22 50L6 68"/>
    <path d="M46 8h18M50 8v40a5 5 0 0010 0V8"/><path d="M50 30h10"/><circle cx="24" cy="12" r="4"/><circle cx="36" cy="18" r="3"/>
  </svg>
  <h3 style="margin-top:14px">Research<br>and Development</h3>
  <span class="zh">研究與開發</span>
  <p style="font-weight:400">Lumo Pharma is a pharmaceutical company registered in Shanghai China.</p>
</div>
<div class="card card-line">
  <svg width="78" height="78" viewBox="0 0 78 78" fill="none" stroke="#7a4429" stroke-width="2">
    <ellipse cx="39" cy="39" rx="36" ry="14"/><ellipse cx="39" cy="39" rx="36" ry="14" transform="rotate(60 39 39)"/><ellipse cx="39" cy="39" rx="36" ry="14" transform="rotate(120 39 39)"/>
    <circle cx="39" cy="39" r="9"/><circle cx="39" cy="39" r="4"/>
  </svg>
  <h3 style="margin-top:14px">Technical support</h3>
  <span class="zh">技術支持</span>
  <p>Lumo Pharma is a pharmaceutical company registered in Shanghai China.</p>
</div>

<!-- news -->
<div class="abs news-band"></div>
<div class="abs section-title serif" style="left:0;width:1200px;top:1888px;text-align:center">NEWS<span class="zh">新聞</span></div>
<p class="abs" style="left:290px;top:1944px;width:620px;text-align:center">Lumo Pharma is a pharmaceutical company registered in Shanghai China, 2019, committed to Chinese traditional herbal medicine, including research and development</p>

<div class="abs news-img" style="left:114px;top:2043px;background:linear-gradient(135deg,#ecebea,#8a5a3a 60%,#e8e6e3)" role="img" aria-label="Wooden spice grinders and a bowl of bay leaves"></div>
<div class="abs news-text" style="left:386px;top:2068px">
  <div class="news-date">April 25, 2020</div>
  <div class="news-title">Industry News</div>
  <div class="news-zh zh">行業新聞</div>
  <p>Lumo Pharma is a pharmaceutical company registered in Shanghai China.</p>
</div>
<div class="abs news-img" style="left:620px;top:2043px;background:radial-gradient(ellipse at 50% 50%,#b07a3a 0,#d7b98d 40%,#8a5634 58%,#ebeae8 62%)" role="img" aria-label="Dried cordyceps on a wooden slice"></div>
<div class="abs news-text" style="left:893px;top:2068px">
  <div class="news-date">April 25, 2020</div>
  <div class="news-title">Company News</div>
  <div class="news-zh zh">公司新聞</div>
  <p>Lumo Pharma is a pharmaceutical company registered in Shanghai China.</p>
</div>
<div class="btn" style="left:503px;top:2335px;width:186px;height:46px">MORE NEWS</div>

<!-- contact -->
<div class="abs contact"></div>
<div class="abs contact-left" role="img" aria-label="Pile of dried cordyceps herbs"></div>
<div class="abs contact-right" role="img" aria-label="Herbal tea cup with dried fruits, cinnamon and herbs"></div>
<div class="abs section-title serif" style="left:0;width:1200px;top:2560px;text-align:center">CONTACT FORM<span class="zh">聯繫表</span></div>
<p class="abs" style="left:370px;top:2614px;width:460px;text-align:center">Lumo Pharma is a pharmaceutical company registered in Shanghai China, 2019, committed to Chinese traditional herbal.</p>
<div class="field" style="left:292px;top:2715px;width:287px;height:44px">Name</div>
<div class="field" style="left:292px;top:2771px;width:287px;height:45px">Email</div>
<div class="field" style="left:594px;top:2715px;width:309px;height:99px;border-radius:14px">Message</div>
<div class="btn" style="left:289px;top:2839px;width:613px;height:45px">SEND MESSAGE</div>

<!-- footer -->
<footer class="abs footer"></footer>
<div class="abs f-brand serif"><span class="f-dot"></span>Lumo Pharma</div>
<div class="abs f-h" style="left:114px;top:3216px;font-size:16px">Lumo Pharmaceutical (Shanghai) Co., Ltd.</div>
<div class="abs f-zh" style="left:114px;top:3242px">露茂醫藥(上海)有限公司</div>
<div class="abs f-small" style="left:114px;top:3274px">Copyright © 2020 Lumo Pharmaceutical (Shanghai) Co., Ltd.</div>

<div class="abs f-h" style="left:559px;top:3096px">Other Agencies</div>
<div class="abs f-zh" style="left:559px;top:3120px">其他代理商</div>
<div class="abs f-small" style="left:559px;top:3151px">東方產業發展協作會<br>華東藥品品質交流中心<br>草本醫藥研究聯盟<br>亞洲保健品貿易協會<br>本草文化協會<br>青溪中藥研究所<br>南山藥用植物研究中心</div>

<div class="abs f-h" style="left:902px;top:3096px">Adress</div>
<div class="abs f-zh" style="left:902px;top:3120px">地址</div>
<div class="abs f-small" style="left:902px;top:3151px">上海市浦東新區青禾路88號</div>
<div class="abs f-h" style="left:902px;top:3216px">Registration No.</div>
<div class="abs f-zh" style="left:902px;top:3242px">註冊號碼。</div>
<div class="abs f-small" style="left:902px;top:3274px">滬備案號 0000000000000號</div>

</body>
</html>
```